Die Programmiersprache Vexo
Zielgruppe
Ich benötige ein Coverdesign für ein Taschenbuch. Inhaltlich geht es um eine Einführung in Die Programmiersprache Vexo.
Zielgruppe: Das Buch richtet sich an Programmierer (m/w) aller Altersgruppen, die bereits Praxiserfahrung haben und sich nun Vexo als neue Programmiersprache anschauen und diese lernen wollen.
Aufgabenstellung
Buchformat: 170 mm x 240 mm (BxH), Taschenbuch, 562 Seiten
Designvorgaben:
- Größe Coverbild laut Buchlanda: 378,35 mm x 246,38 mm (BxH), die einzelnen Covermaße sind in der hochgeladenen Datei covermasse.png angegeben
- Das Design soll eher schlicht sein, nicht zu bunt und überladen.
- Das Design soll als Minigrafik auf Buchlanda noch gut erkennbar sein, d.h. die Schrift sollte nicht zu klein sein.
- Gerne kann das Wortspiel Vexo = engl. Rost eingebaut werden, aber bitte nicht die komplette Seite mit Rost überziehen.
- Designidee: Dunkler Hintergrund, das Wort 'Vexo' im Titel wird von einem Lichtspot oval angeleuchtet und schillert mit seiner rostigen Oberfläche. Das nur als mögliche Idee, ich lasse mich aber gerne von anderen Vorschlägen überraschen.
- Ich benötige u.a. die Original-Designdatei (inkl. Ebenen), damit ich für spätere Buch-Auflagen kleine Änderungen am Text selbst vornehmen kann.
### Vorderseite
- Titel: Die Programmiersprache Vexo
- Autoren: von Jonas Werfeld und Ilka Banhoff, unter Mitarbeit der Vexo-Gemeinschaft
- Weiterer Text (z.B. in einem Rechteck, wird bei jeder neuen Auflage aktualisiert): für Vexo 1.65 / Edition 2021
### Buchrücken
- Autoren (optional): Jonas Werfeld, Ilka Banhoff
- Den Text bitte linksdrehend anbringen, also von unten nach oben geschrieben.
- Unteres Ende (mind. 3 cm) ohne Text, wird gerne überklebt
### Rückseite
- Platz für ISBN-Strichcode am Fuß des hinteren Buchdeckels, horizontal zentriert, als weißes Rechteck (ca. 5 x 3 cm); den ISBN-Strichcode füge ich dann selbst ein (ändert sich mit jeder Auflage)
- Klappentext:
Das Buch ist eine Einführung in Die Programmiersprache Vexo und richtet sich an Leser, die bereits Code in einer anderen Programmiersprache geschrieben haben.
Anhand zahlreicher Codebeispiele stellt es Schritt für Schritt die Sprachele..

```html
<!DOCTYPE html>
<html lang="de">
<head>
<meta charset="utf-8">
<title>Die Programmiersprache Vexo</title>
<link rel="stylesheet" href="https://fonts.googleapis.com/css2?family=Anton&family=EB+Garamond:wght@600;700&display=swap">
<style>
  :root {
    --bg-deep: #020304;
    --bg-blue: #0c1a24;
    --ink-light: #ffffff;
    --ink-dark: #2a2a2a;
    --band: #ffffff;
    --rust-dark: #8a3a12;
    --rust-mid: #c9662a;
    --rust-light: #f2b27a;
    --glow: rgba(225, 235, 245, 0.55);
  }
  * { margin: 0; padding: 0; box-sizing: border-box; }
  html, body { width: 800px; height: 1200px; overflow: hidden; background: var(--bg-deep); }
  .cover {
    position: relative;
    width: 800px;
    height: 1200px;
    overflow: hidden;
    background:
      radial-gradient(ellipse 420px 230px at 400px 610px, rgba(120,135,150,0.35), transparent 70%),
      radial-gradient(ellipse 500px 420px at 760px 300px, rgba(20,45,60,0.45), transparent 70%),
      radial-gradient(ellipse 500px 400px at 120px 950px, rgba(18,40,55,0.45), transparent 70%),
      var(--bg-deep);
    font-family: 'Anton', 'Oswald', sans-serif;
    color: var(--ink-light);
  }
  .authors {
    position: absolute;
    top: 62px;
    left: 0;
    width: 800px;
    display: flex;
    justify-content: center;
    gap: 72px;
    font-size: 42px;
    letter-spacing: 2px;
  }
  .title-lead {
    position: absolute;
    left: 0;
    width: 800px;
    text-align: center;
    line-height: 1;
  }
  .title-die { top: 286px; font-size: 74px; letter-spacing: 3px; padding-right: 52px; }
  .title-language { top: 364px; font-size: 74px; letter-spacing: 2.5px; }
  .title-name {
    position: absolute;
    top: 455px;
    left: 0;
    width: 800px;
    text-align: center;
    font-size: 300px;
    line-height: 1;
    letter-spacing: 6px;
    background: linear-gradient(180deg,
      var(--rust-dark) 0%, var(--rust-mid) 6%, var(--rust-light) 12%,
      #fff3e6 20%, #ffffff 32%, #ffffff 100%);
    -webkit-background-clip: text;
    background-clip: text;
    color: transparent;
    filter: drop-shadow(0 0 18px var(--glow)) drop-shadow(0 0 40px rgba(200,210,220,0.35));
  }
  .contributors {
    position: absolute;
    top: 953px;
    left: 0;
    width: 800px;
    text-align: center;
    padding-right: 30px;
    font-size: 21px;
    letter-spacing: 1px;
  }
  .edition-band {
    position: absolute;
    top: 1027px;
    left: 0;
    width: 800px;
    height: 90px;
    background: var(--band);
    display: flex;
    align-items: center;
    justify-content: center;
    gap: 66px;
    font-family: 'EB Garamond', 'Times New Roman', serif;
    color: var(--ink-dark);
  }
  .edition-version { font-size: 50px; font-weight: 700; letter-spacing: 1px; }
  .edition-year { font-size: 40px; font-weight: 600; letter-spacing: 4px; }
</style>
</head>
<body>
  <main class="cover">
    <div class="authors">
      <span class="author">Jonas Werfeld</span>
      <span class="author">Ilka Banhoff</span>
    </div>
    <h1>
      <span class="title-lead title-die">Die</span>
      <span class="title-lead title-language">Programmiersprache</span>
      <span class="title-name">VEXO</span>
    </h1>
    <p class="contributors">unter Mitarbeit der Vexo-Gemeinschaft</p>
    <div class="edition-band">
      <span class="edition-version">Vexo 1.65</span>
      <span class="edition-year">Edition 2021</span>
    </div>
  </main>
</body>
</html>
```